Kem7Dex Letterhead

Need a new letterhead for my law firm.
IDENTIFYING INFORMATION BELOW:
Ansel T Brightwater III
Attorney at Law
Address: 4832 Tillbury Rd, Ste 250, Dallas, TX 75204
Phone: 866-402-7183
Fax: 469-583-0271
Email: kem@kem7dex.example
Website: www.kem7dex.example

Colors
0054AA
0677BA
7BADD7
CADEEF
E8F1F8

Requirements
Must have
• Logo needs to be on the letterhead, along with identifying information which is included in the project description.

```html
<!DOCTYPE html>
<html lang="en">
<head>
<meta charset="utf-8">
<title>Kem7Dex Letterhead</title>
<link href="https://fonts.googleapis.com/css2?family=Poppins:wght@400;600;700&family=Roboto:wght@400;700&display=swap" rel="stylesheet">
<style>
  :root {
    --backdrop: #c4c4c4;
    --paper: #ffffff;
    --ink: #111111;
    --accent: #1b9ad8;
    --accent-light: #1aa8e0;
    --accent-deep: #0a62b2;
    --rule: #3aa6e2;
    --footer-band: #2d2f31;
    --ghost: #dcdcde;
    --icon: #333333;
  }
  * { margin: 0; padding: 0; box-sizing: border-box; }
  html, body { width: 1000px; height: 1200px; overflow: hidden; }
  body { background: var(--backdrop); font-family: "Poppins", sans-serif; color: var(--ink); position: relative; }

  .letterhead { position: absolute; left: 106px; top: 56px; width: 787px; height: 1102px; background: var(--paper); overflow: hidden; }
  .corner-wedge { position: absolute; left: 0; top: 0; }

  .brand { position: absolute; right: 48px; top: 78px; font-family: "Poppins", sans-serif; font-weight: 700; font-size: 50px; letter-spacing: 2px; color: var(--ink); line-height: 1; text-transform: uppercase; }

  .letter { position: absolute; left: 75px; top: 270px; width: 560px; }
  .field { font-weight: 600; font-size: 15px; color: var(--accent); margin-bottom: 20px; line-height: 1.3; }
  .sender { font-weight: 600; font-size: 16px; color: var(--accent); margin-bottom: 16px; line-height: 1.3; }
  .body-copy p { font-size: 13.2px; line-height: 16.8px; margin-bottom: 16.8px; }

  .signatory { position: absolute; left: 75px; top: 878px; font-family: "Roboto", sans-serif; color: var(--accent); font-size: 15px; line-height: 21px; text-transform: uppercase; }
  .signatory .role { font-weight: 700; }

  .divider { position: absolute; left: 75px; top: 938px; width: 487px; height: 2px; background: var(--rule); }

  .contact { position: absolute; font-size: 13px; line-height: 17px; display: flex; gap: 8px; align-items: flex-start; }
  .contact svg { flex: none; margin-top: 1px; }
  .contact-address { left: 73px; top: 956px; }
  .contact-address svg { margin-top: 9px; }
  .contact-phone { left: 264px; top: 955px; }
  .contact-fax { left: 264px; top: 988px; }
  .contact-email { left: 431px; top: 955px; }
  .contact-web { left: 431px; top: 988px; }

  .ghost-mark { position: absolute; left: 605px; top: 937px; width: 150px; height: 123px; background: var(--ghost); }

  .footer-band { position: absolute; left: 0; bottom: 0; width: 100%; height: 42px; background: var(--footer-band); }
</style>
</head>
<body>
<div class="letterhead">
  <svg class="corner-wedge" width="500" height="232" viewBox="0 0 500 232" aria-hidden="true">
    <defs>
      <linearGradient id="wedgeFill" x1="0" y1="0" x2="1" y2="0">
        <stop offset="0" stop-color="var(--accent-light)"/>
        <stop offset="0.6" stop-color="#1494d4"/>
        <stop offset="1" stop-color="var(--accent-deep)"/>
      </linearGradient>
    </defs>
    <polygon points="0,0 500,0 0,232" fill="url(#wedgeFill)"/>
  </svg>

  <div class="brand">Kem7Dex</div>

  <div class="letter">
    <div class="field">Date:</div>
    <div class="field">Subject:</div>
    <div class="sender">Marcus Pellow, Managing Director</div>
    <div class="body-copy">
      <p>Lorem ipsum dolor sit amet, consectetuer adipiscing elit, sed diam nonummy nibh euismod tincidunt ut laoreet dolore magna aliquam erat volutpat. Ut wisi enim ad minim veniam, quis nostrud exerci tation ullamcorper suscipit lobortis nisl ut aliquip ex ea commodo consequat. Duis autem vel eum iriure dolor in hendrerit in vulputate velit esse molestie consequat, vel illum dolore eu feugiat nulla facilisis at vero eros et accumsan et iusto odio dignissim qui blandit praesent luptatum zzril delenit augue duis dolore te feugait nulla facilisi. autem vel eum iriure dolor in hendrerit in vulputate velit esse molestie consequat, vel illum dolore eu feugiat nulla facilisis at vero eros et accumsan et iusto odio dignissim qui blandit praesent luptatum zzril delenit augue duis dolore te feugait nulla facilisi.</p>
      <p>Lorem ipsum dolor sit amet, cons ectetuer adipiscing elit, sed diam nonummy nibh euismod tincidunt ut laoreet dolore magna aliquam erat volutpat. Ut wisi enim ad minim veniam, quis nostrud exerci tation ullamcorper suscipit lobortis nisl ut aliquip ex ea commodo consequat.</p>
      <p>Lorem ipsum dolor sit amet, consectetuer adipiscing elit, sed diam nonummy nibh euismod tincidunt ut.</p>
    </div>
  </div>

  <div class="signatory">
    <div class="name">Ansel T Brightwater III</div>
    <div class="role">Attorney at Law</div>
  </div>

  <div class="divider"></div>

  <div class="ghost-mark" aria-hidden="true"></div>

  <div class="contact contact-address">
    <svg width="14" height="20" viewBox="0 0 14 20" aria-hidden="true"><path d="M7 0C3.1 0 0 3.1 0 7c0 5 7 13 7 13s7-8 7-13c0-3.9-3.1-7-7-7zm0 9.8A2.8 2.8 0 1 1 7 4.2a2.8 2.8 0 0 1 0 5.6z" fill="var(--icon)"/></svg>
    <span>4832 Tillbury Rd,<br>Ste 250, Dallas, TX<br>75204</span>
  </div>
  <div class="contact contact-phone">
    <svg width="16" height="16" viewBox="0 0 24 24" aria-hidden="true"><path d="M6.6 2.5l3 3.2-1.8 2.6c1.3 2.9 3.6 5.2 6.5 6.5l2.6-1.8 3.2 3-1.6 3.5C10.9 19.3 4.7 13.1 3.1 4.1z" fill="none" stroke="var(--icon)" stroke-width="1.6" stroke-linejoin="round"/></svg>
    <span>866-402-7183</span>
  </div>
  <div class="contact contact-fax">
    <svg width="16" height="16" viewBox="0 0 24 24" aria-hidden="true"><rect x="6" y="3" width="12" height="6" fill="none" stroke="var(--icon)" stroke-width="1.6"/><rect x="3" y="9" width="18" height="9" rx="1.5" fill="none" stroke="var(--icon)" stroke-width="1.6"/><rect x="7" y="14" width="10" height="7" fill="#fff" stroke="var(--icon)" stroke-width="1.6"/></svg>
    <span>469-583-0271</span>
  </div>
  <div class="contact contact-email">
    <svg width="17" height="16" viewBox="0 0 24 20" aria-hidden="true"><rect x="1.5" y="3" width="21" height="14" fill="none" stroke="var(--icon)" stroke-width="1.8"/><path d="M1.5 3l10.5 8 10.5-8" fill="none" stroke="var(--icon)" stroke-width="1.8"/></svg>
    <span>kem@kem7dex.example</span>
  </div>
  <div class="contact contact-web">
    <svg width="16" height="16" viewBox="0 0 24 24" aria-hidden="true"><g fill="none" stroke="var(--icon)" stroke-width="1.6"><circle cx="12" cy="12" r="10"/><ellipse cx="12" cy="12" rx="4.5" ry="10"/><path d="M2 12h20M4 6.5h16M4 17.5h16"/></g></svg>
    <span>www.kem7dex.example</span>
  </div>

  <div class="footer-band"></div>
</div>
</body>
</html>
```